BrightKeel Business Card Contest

We are looking for a modern business card that catches attention and is unique. Attached is the brand guide and logo files. Please note that the back side (not the side with our name and info) with be UV raise printed, so have fun with the design there. We want to include Name, Title, Phone number, email, website.

Contact Information for Business Card

Please see project description

```html
<!DOCTYPE html>
<html lang="en">
<head>
<meta charset="utf-8">
<title>BrightKeel Business Card</title>
<link rel="stylesheet" href="https://fonts.googleapis.com/css2?family=Montserrat:wght@400;600;700&display=swap">
<style>
  :root {
    --backdrop: #2b2c2e;
    --card: #1c1c1d;
    --cyan: #18b6df;
    --white: #f4f5f6;
    --raised: #2e2e30;
  }
  * { box-sizing: border-box; margin: 0; padding: 0; }
  html, body {
    width: 1027px;
    height: 1200px;
    overflow: hidden;
    background: var(--backdrop);
    font-family: "Montserrat", sans-serif;
  }
  .sheet {
    position: relative;
    width: 1027px;
    height: 1200px;
  }
  .card {
    position: absolute;
    left: 93px;
    width: 840px;
    height: 480px;
    background: var(--card);
    border-bottom: 6px solid var(--cyan);
    overflow: hidden;
  }
  .card--front { top: 70px; }
  .card--back { top: 640px; }

  /* front */
  .wordmark {
    position: absolute;
    display: flex;
    align-items: center;
    gap: 18px;
    font-weight: 600;
    letter-spacing: -1px;
    color: var(--white);
  }
  .card--front .wordmark {
    right: 60px;
    top: 110px;
    font-size: 74px;
  }
  .wordmark__square {
    width: 40px;
    height: 40px;
    background: var(--cyan);
  }
  .divider {
    position: absolute;
    left: 120px;
    right: 50px;
    top: 262px;
    height: 2px;
    background: var(--cyan);
  }
  .accent {
    position: absolute;
    left: 60px;
    top: 206px;
    width: 34px;
    height: 34px;
    background: var(--cyan);
  }
  .person {
    position: absolute;
    left: 118px;
    top: 198px;
  }
  .person__name {
    font-size: 26px;
    font-weight: 700;
    letter-spacing: 0.5px;
    color: var(--cyan);
    text-transform: uppercase;
  }
  .person__title {
    font-size: 18px;
    font-weight: 400;
    color: var(--white);
    margin-top: 2px;
  }
  .contact {
    position: absolute;
    left: 140px;
    top: 286px;
    list-style: none;
  }
  .contact__item {
    display: flex;
    align-items: center;
    gap: 12px;
    font-size: 19px;
    color: var(--white);
    height: 32px;
  }
  .contact__icon {
    width: 18px;
    height: 18px;
    flex: none;
  }
  .address {
    position: absolute;
    right: 60px;
    top: 286px;
    text-align: right;
    font-style: normal;
    font-size: 19px;
    line-height: 32px;
    color: var(--white);
  }

  /* back */
  .card--back .wordmark {
    left: 50%;
    top: 50%;
    transform: translate(-50%, -50%);
    font-size: 96px;
    color: var(--raised);
  }
  .card--back .wordmark__square {
    width: 56px;
    height: 56px;
    background: var(--raised);
  }
</style>
</head>
<body>
<main class="sheet">
  <section class="card card--front" aria-label="Business card front">
    <div class="wordmark"><span class="wordmark__square"></span><span>BrightKeel</span></div>
    <span class="accent"></span>
    <div class="person">
      <p class="person__name">Daniel Harlow</p>
      <p class="person__title">Manager</p>
    </div>
    <span class="divider"></span>
    <ul class="contact">
      <li class="contact__item">
        <svg class="contact__icon" viewBox="0 0 24 24" fill="none" stroke="#18b6df" stroke-width="2" stroke-linecap="round" stroke-linejoin="round"><path d="M22 16.9v3a2 2 0 0 1-2.2 2 19.8 19.8 0 0 1-8.6-3.1 19.5 19.5 0 0 1-6-6A19.8 19.8 0 0 1 2.1 4.2 2 2 0 0 1 4.1 2h3a2 2 0 0 1 2 1.7c.1 1 .4 1.9.7 2.8a2 2 0 0 1-.5 2.1L8 9.8a16 16 0 0 0 6 6l1.3-1.3a2 2 0 0 1 2.1-.4c.9.3 1.8.6 2.8.7a2 2 0 0 1 1.8 2z"/></svg>
        <span>123-555-0148</span>
      </li>
      <li class="contact__item">
        <svg class="contact__icon" viewBox="0 0 24 24" fill="none" stroke="#18b6df" stroke-width="2" stroke-linejoin="round"><rect x="2" y="5" width="20" height="14" rx="1"/><path d="M2 6l10 7 10-7"/></svg>
        <span>hello@brightkeel.com</span>
      </li>
      <li class="contact__item">
        <svg class="contact__icon" viewBox="0 0 24 24" fill="none" stroke="#18b6df" stroke-width="2"><circle cx="12" cy="12" r="10"/><path d="M2 12h20M12 2a15 15 0 0 1 0 20M12 2a15 15 0 0 0 0 20"/></svg>
        <span>www.brightkeel.com</span>
      </li>
    </ul>
    <address class="address">Your Address<br>City, State, Zip 0000</address>
  </section>

  <section class="card card--back" aria-label="Business card back">
    <div class="wordmark"><span class="wordmark__square"></span><span>BrightKeel</span></div>
  </section>
</main>
</body>
</html>
```